Corvento Franchise Services
Design business cards , stationery and banner
Creater,
The ai file is included in the zip folder.
Thanks for the design so far. Can you make sure you include business cards and stationery in your submissions. Thanks
sir plzz upload the logo in ai file

```html
<!DOCTYPE html>
<html lang="en">
<head>
<meta charset="utf-8">
<title>Corvento Franchise Services – Stationery Set</title>
<link href="https://fonts.googleapis.com/css2?family=Cinzel:wght@400;600&display=swap" rel="stylesheet">
<style>
  :root {
    --navy: #0f3a6b;
    --blue: #1d5fa8;
    --blue-light: #4fa3dc;
    --green: #7fae2e;
    --green-light: #c7e26b;
    --ink: #2a3440;
    --paper: #ffffff;
    --edge: #d4d8dd;
  }
  * { margin: 0; padding: 0; box-sizing: border-box; }
  html, body { width: 1200px; height: 730px; overflow: hidden; background: var(--paper); }
  body { position: relative; font-family: "Cinzel", serif; color: var(--ink); }

  .sheet { position: absolute; background: var(--paper); border: 1px solid var(--edge); box-shadow: 0 1px 4px rgba(0,0,0,.12); overflow: hidden; }

  .brand { position: absolute; display: flex; align-items: center; gap: 8px; color: var(--navy); font-family: "Cinzel", serif; font-weight: 600; }
  .brand-dot { border-radius: 50%; background: var(--blue); flex: none; }
  .brand-name { line-height: 1; }
  .brand-name .line-main { display: block; letter-spacing: .02em; }
  .brand-name .line-sub { display: block; letter-spacing: .18em; margin-top: 3px; }

  /* letterhead */
  .letterhead { left: 48px; top: 12px; width: 500px; height: 703px; }
  .letterhead .swoosh { position: absolute; left: 0; top: 0; }
  .letterhead .brand { left: 20px; top: 40px; }
  .letterhead .brand-dot { width: 34px; height: 34px; }
  .letterhead .line-main { font-size: 30px; }
  .letterhead .line-sub { font-size: 9px; }
  .letterhead-footer { position: absolute; left: 14px; bottom: 14px; font-size: 8.5px; line-height: 13px; color: var(--navy); letter-spacing: .03em; }

  /* business card front */
  .card-front { left: 571px; top: 36px; width: 233px; height: 137px; }
  .card-front .brand { left: 10px; top: 10px; gap: 5px; }
  .card-front .brand-dot { width: 16px; height: 16px; }
  .card-front .line-main { font-size: 15px; }
  .card-front .line-sub { font-size: 5px; margin-top: 2px; }
  .card-person { position: absolute; left: 0; right: 0; top: 44px; text-align: center; color: var(--navy); }
  .card-person .person-name { font-size: 8px; font-weight: 600; letter-spacing: .05em; }
  .card-person .person-role { font-size: 5.5px; margin-top: 1px; }
  .card-details { position: absolute; left: 10px; top: 72px; font-size: 5.5px; line-height: 9px; color: var(--ink); }

  /* business card back, white */
  .card-back { left: 828px; top: 96px; width: 221px; height: 132px; }
  .card-back .brand { left: 36px; top: 50px; gap: 6px; }
  .card-back .brand-dot { width: 22px; height: 22px; }
  .card-back .line-main { font-size: 20px; }
  .card-back .line-sub { font-size: 6px; }

  /* colour card backs */
  .card-colour { top: 240px; height: 127px; border: none; }
  .card-green { left: 619px; width: 216px; background: radial-gradient(circle at 50% 48%, var(--green-light) 0%, var(--green) 55%, #5e8a1f 100%); }
  .card-blue { left: 864px; width: 228px; background: radial-gradient(circle at 50% 48%, #8fd0f2 0%, var(--blue-light) 25%, var(--blue) 60%, var(--navy) 100%); }
  .card-colour .brand { left: 50%; top: 50%; transform: translate(-50%, -50%); color: #fff; gap: 6px; }
  .card-colour .brand-dot { width: 20px; height: 20px; background: #fff; }
  .card-colour .line-main { font-size: 14px; }
  .card-colour .line-sub { font-size: 5px; }

  /* envelope */
  .envelope { left: 576px; top: 379px; width: 533px; height: 336px; }
  .envelope .flap { position: absolute; left: 0; top: 0; }
  .envelope .brand { left: 14px; top: 112px; }
  .envelope .brand-dot { width: 30px; height: 30px; }
  .envelope .line-main { font-size: 26px; }
  .envelope .line-sub { font-size: 8px; }
  .envelope-address { position: absolute; left: 14px; top: 234px; font-size: 10px; line-height: 15px; color: var(--navy); letter-spacing: .03em; }
</style>
</head>
<body>

<section class="sheet letterhead" aria-label="Letterhead">
  <svg class="swoosh" width="500" height="60" viewBox="0 0 500 60" aria-hidden="true">
    <defs>
      <linearGradient id="swooshFill" x1="0" x2="1" y1="0" y2="0">
        <stop offset="0" stop-color="#1d5fa8" stop-opacity="0.2"/>
        <stop offset="0.5" stop-color="#1d5fa8"/>
        <stop offset="1" stop-color="#0f3a6b"/>
      </linearGradient>
    </defs>
    <path d="M0 0 H500 V22 C380 8 200 6 0 14 Z" fill="url(#swooshFill)"/>
  </svg>
  <div class="brand">
    <span class="brand-dot"></span>
    <span class="brand-name"><span class="line-main">CORVENTO</span><span class="line-sub">FRANCHISE SERVICES</span></span>
  </div>
  <address class="letterhead-footer" style="font-style:normal">
    14 Larch Row, Westbrae, Glasgow, G71 4PT<br>
    Phone 01355 410 822 | Cell 07700 900 415 | Fax 01355 410 823<br>
    Email: info@corventofs.co.uk | www.corventofs.co.uk
  </address>
</section>

<section class="sheet card-front" aria-label="Business card front">
  <div class="brand">
    <span class="brand-dot"></span>
    <span class="brand-name"><span class="line-main">CORVENTO</span><span class="line-sub">FRANCHISE SERVICES</span></span>
  </div>
  <div class="card-person">
    <div class="person-name">MORVEN ASHDALE</div>
    <div class="person-role">Managing Director</div>
  </div>
  <div class="card-details">
    14 Larch Row<br>
    Westbrae, Glasgow G71 4PT<br>
    Phone 01355 410 822 | Cell 07700 900 415<br>
    morven@corventofs.co.uk
  </div>
</section>

<section class="sheet card-back" aria-label="Business card back">
  <div class="brand">
    <span class="brand-dot"></span>
    <span class="brand-name"><span class="line-main">CORVENTO</span><span class="line-sub">FRANCHISE SERVICES</span></span>
  </div>
</section>

<section class="sheet card-colour card-green" aria-label="Business card back, green">
  <div class="brand">
    <span class="brand-dot"></span>
    <span class="brand-name"><span class="line-main">CORVENTO</span><span class="line-sub">FRANCHISE SERVICES</span></span>
  </div>
</section>

<section class="sheet card-colour card-blue" aria-label="Business card back, blue">
  <div class="brand">
    <span class="brand-dot"></span>
    <span class="brand-name"><span class="line-main">CORVENTO</span><span class="line-sub">FRANCHISE SERVICES</span></span>
  </div>
</section>

<section class="sheet envelope" aria-label="Envelope">
  <svg class="flap" width="533" height="110" viewBox="0 0 533 110" aria-hidden="true">
    <defs>
      <radialGradient id="flapFill" cx="0.5" cy="0.45" r="0.6">
        <stop offset="0" stop-color="#6cc0ec"/>
        <stop offset="0.3" stop-color="#2f7fc4"/>
        <stop offset="1" stop-color="#0f3a6b"/>
      </radialGradient>
    </defs>
    <path d="M0 0 H533 V60 C400 88 200 100 0 82 Z" fill="url(#flapFill)"/>
    <path d="M0 82 C200 100 400 88 533 60" fill="none" stroke="#7fae2e" stroke-width="2"/>
  </svg>
  <div class="brand">
    <span class="brand-dot"></span>
    <span class="brand-name"><span class="line-main">CORVENTO</span><span class="line-sub">FRANCHISE SERVICES</span></span>
  </div>
  <address class="envelope-address" style="font-style:normal">
    14 Larch Row<br>
    Westbrae, Glasgow, G71 4PT
  </address>
</section>

</body>
</html>
```